Creation of a construction/bricklaying business website

Following the template format of "Wendmoor 2", the following content would need to be included:
1. Landing page with 3 tiles that go to their own pages.
- Landing page to include background photo and description of services offered.
2. 3 tiles to include:
a) "Contact Us For A Free Quote or Friendly Discussion" Form (middle tile)
b) Case Studies and Testimonials
c) Certifications and Professional Membership
- Design logo to be used from previous PixelHarbor project. Example of logo attached below, please access full JPG files from our account.

Target Market(s)

Prospective clients seeking construction work (bricklaying speciality)

Industry/Entity Type

Residential Construction

Coding

Coded - Design and coding required

Number of Pages Required

4 page

Font styles to use
Sans Serif

Colors

Designer to choose colors to be used in the design.

Requirements
Must have
• Following the template format of "Wendmoor 2", the following content would need to be included:
• 1. Landing parent page with 3 tiles that go to the 3 child pages.
• - Landing page to include background photo and description of services offered.
• 2. 3 tiles to include:
• a) "Contact Us For A Free Quote or Friendly Discussion" Form (middle tile)
• b) Case Studies and Testimonials (first tile / left side)
• c) Certifications and Professional Memberships (third tile / right side) (This should include logos of the relevant organisations being displayed. Specifically QLT and the Keystone Pact QLT).
• - Design logo to be used from previous PixelHarbor project. Example of logo attached below, please access full JPG files from our account.
Nice to have
• Sleek and modern feel.
• Approachable in terms of how people can contact the company for a quote.
• Traditional pictures to give credibility and comfort around choosing this company.
Should not have
• Cheesy pictures
• Over-complicated
• Simple to use
• Easy URL domain name

```html
<!DOCTYPE html>
<html lang="en">
<head>
<meta charset="utf-8">
<title>R.T. Marlow – Construction</title>
<link href="https://fonts.googleapis.com/css2?family=Montserrat:wght@400;600;700&family=Open+Sans:wght@400;600&display=swap" rel="stylesheet">
<style>
:root{
  --blue:#0b4aa8;
  --blue-dark:#083a86;
  --ink:#222;
  --body:#666;
  --light:#f4f4f4;
  --white:#fff;
  --dark:#1b1b1b;
}
*{box-sizing:border-box;margin:0;padding:0}
html,body{width:1200px;height:4023px;overflow:hidden}
body{font-family:"Open Sans",Arial,sans-serif;color:var(--body);background:var(--white);font-size:12px;line-height:1.6;position:relative}
h1,h2,h3,h4{font-family:"Montserrat",Arial,sans-serif;color:var(--ink)}
.section-title{text-align:center;font-size:19px;font-weight:700;text-transform:uppercase;letter-spacing:.5px}
.section-title::after{content:"";display:block;width:50px;height:2px;background:var(--blue);margin:12px auto 0}
.abs{position:absolute}

/* top bar + nav */
.topbar{top:0;left:0;width:1200px;height:22px;background:var(--blue);color:#fff;font-size:9px;display:flex;gap:20px;align-items:center;padding-left:262px}
.nav{top:22px;left:0;width:1200px;height:60px;background:#fff;display:flex;align-items:center;justify-content:space-between;padding:0 262px}
.brand{display:flex;align-items:center;gap:8px;font-family:"Montserrat",sans-serif;font-weight:700;font-size:16px;color:var(--blue)}
.brand i{width:14px;height:14px;background:var(--blue);display:block}
.menu{display:flex;gap:22px;font-family:"Montserrat",sans-serif;font-size:10px;text-transform:uppercase;color:#555}
.menu .on{color:var(--blue)}

/* hero */
.hero{top:82px;left:0;width:1200px;height:423px;background:linear-gradient(135deg,#5a4a3a,#8a7559 45%,#6b5b48 70%,#3e342b)}
.hero-title{top:290px;left:0;width:1200px;text-align:center;color:#fff;font-size:40px;font-weight:700;line-height:1.1;text-transform:uppercase;text-shadow:0 2px 6px rgba(0,0,0,.4)}
.tile{background:#fff;text-align:center;padding:18px 22px;box-shadow:0 2px 10px rgba(0,0,0,.12)}
.tile h3{color:var(--blue);font-size:12px;font-weight:600;margin:6px 0;line-height:1.3}
.tile p{font-size:10px;line-height:1.5}
.tile svg{width:30px;height:30px}

/* about */
.about{top:655px;left:0;width:1200px;height:330px;background:var(--light)}
.about .section-title{position:absolute;top:48px;width:100%}
.about-col{position:absolute;top:112px;width:200px}
.about-col h4{color:var(--blue);font-size:12px;text-transform:uppercase;margin-bottom:10px}
.about-col p{font-size:10.5px}

/* services */
.services{top:987px;left:0;width:1200px;height:589px;background:radial-gradient(circle at 50% 40%,#333,#111)}
.services .section-title{position:absolute;top:105px;width:100%;color:#fff}
.service{position:absolute;width:220px;text-align:center;color:#ddd}
.service .ico{width:44px;height:44px;border-radius:50%;background:var(--blue);margin:0 auto 10px;display:flex;align-items:center;justify-content:center}
.service h3{color:#fff;font-size:16px;margin-bottom:6px}
.service p{font-size:10px;line-height:1.5}

/* portfolio */
.portfolio-title{top:1638px;left:0;width:1200px}
.grid{top:1713px;left:0;width:1200px;height:460px;display:grid;grid-template-columns:repeat(4,300px);grid-template-rows:230px 230px}

/* testimonials */
.testi-title{top:2310px;left:0;width:1200px}
.testi{top:2400px;left:0;width:1200px;height:286px;background:linear-gradient(120deg,#0b3f8f,#1558b8 50%,#0a3a82);color:#fff;text-align:center;padding-top:95px}
.testi q{font-family:"Montserrat",sans-serif;font-weight:600;font-size:14px;display:block;margin-bottom:8px}
.testi p{font-size:14px;width:600px;margin:0 auto;line-height:1.5}
.dots{display:flex;gap:6px;justify-content:center;margin-top:50px}
.dots span{width:7px;height:7px;border-radius:50%;background:rgba(255,255,255,.5)}
.dots .on{background:#fff}

/* why us */
.why{top:2700px;left:0;width:1200px;height:410px;background:#f7f7f7}
.why-img{position:absolute;left:262px;top:71px;width:202px;height:289px;background:linear-gradient(160deg,#c9a46b,#8c6a3e)}
.why-text{position:absolute;left:499px;top:62px;width:440px}
.why-text h2{font-size:21px;text-transform:uppercase;margin-bottom:6px}
.why-text h4{color:var(--blue);font-family:"Open Sans",sans-serif;font-weight:400;font-size:14px;margin-bottom:10px}
.why-text p{font-size:10.5px;margin-bottom:12px}

/* news */
.news-title{top:3170px;left:0;width:1200px}
.news{position:absolute;top:3259px;width:188px}
.news .ph{height:114px;background:linear-gradient(135deg,#aab4bf,#5d6a78)}
.news h4{color:var(--blue);font-size:12px;margin:12px 0 6px}
.news p{font-size:10px;line-height:1.5}

/* cta */
.cta{top:3504px;left:0;width:1200px;height:142px;background:var(--blue);display:flex;align-items:center;justify-content:space-between;padding:0 262px;color:#fff;font-size:16px}
.btn{border:1.5px solid #fff;border-radius:16px;padding:6px 20px;font-size:11px;font-family:"Montserrat",sans-serif;text-transform:uppercase}

/* contact */
.contact{top:3646px;left:0;width:1200px;height:314px;background:#f4f4f4}
.contact .section-title{position:absolute;top:58px;width:100%}
.c-item{position:absolute;top:150px;width:170px;text-align:center}
.c-item svg{width:28px;height:28px}
.c-item h4{color:var(--blue);font-size:10px;text-transform:uppercase;margin:8px 0 4px}
.c-item p{font-size:10px;line-height:1.5}

footer{top:3960px;left:0;width:1200px;height:63px;background:var(--blue);color:#fff;text-align:center;font-size:10px;padding-top:8px}
.social{display:flex;gap:4px;justify-content:center;margin-bottom:8px}
.social span{width:16px;height:16px;background:#fff;opacity:.85;display:block}
</style>
</head>
<body>

<div class="abs topbar"><span>✆ (555) 014-2290</span><span>✉ hello@rtmarlow.example</span></div>
<header class="abs nav">
  <div class="brand"><i></i>R.T. Marlow</div>
  <nav class="menu"><span class="on">Home</span><span>About us</span><span>Services</span><span>Contact</span></nav>
</header>

<section class="abs hero" role="img" aria-label="Builder in hard hat above a workbench with blueprints, level, calculator and tools"></section>
<h1 class="abs hero-title">Committed to superior<br>quality and results</h1>

<div class="abs tile" style="left:245px;top:436px;width:232px;height:150px">
  <svg viewBox="0 0 30 30" fill="none" stroke="#0b4aa8" stroke-width="2"><path d="M4 8h16v10H10l-6 5z"/><path d="M22 12h4v10l-4-3h-8v-1"/></svg>
  <h3>Case Studies &amp; Testimonials</h3>
  <p>See homes and walls we have built and read what our clients say about working with us.</p>
</div>
<div class="abs tile" style="left:491px;top:417px;width:223px;height:169px;padding-top:26px">
  <svg viewBox="0 0 30 30" fill="none" stroke="#0b4aa8" stroke-width="2"><rect x="4" y="7" width="22" height="16"/><path d="M4 7l11 8 11-8"/></svg>
  <h3>Contact Us For A Free Quote or Friendly Discussion</h3>
  <p>Tell us about your project and we will get back to you with a clear, free quote.</p>
</div>
<div class="abs tile" style="left:728px;top:436px;width:213px;height:150px">
  <svg viewBox="0 0 30 30" fill="none" stroke="#0b4aa8" stroke-width="2"><circle cx="15" cy="12" r="7"/><path d="M10 18l-2 9 7-3 7 3-2-9"/></svg>
  <h3>Certifications &amp; Memberships</h3>
  <p>Our licences and our QLT and Keystone Pact QLT memberships, all in one place.</p>
</div>

<section class="abs about">
  <h2 class="section-title">About R.T. Marlow</h2>
  <div class="about-col" style="left:262px"><h4>Motivation</h4><p>We build homes people live in for decades. Every course of brick is set to last, checked by hand and finished clean before we move on.</p></div>
  <div class="about-col" style="left:499px"><h4>History</h4><p>Started as a two-person crew, we now run full teams on homes and extensions across the region, with the same hands-on care.</p></div>
  <div class="about-col" style="left:736px"><h4>Certificates</h4><p>Our trades hold current licences and memberships, and our work meets the codes and standards your project requires.</p></div>
</section>

<section class="abs services">
  <h2 class="section-title">Services</h2>
  <div class="service" style="left:253px;top:187px"><div class="ico"><svg width="18" height="18" viewBox="0 0 18 18" fill="none" stroke="#fff" stroke-width="1.6"><rect x="3" y="2" width="12" height="14"/><path d="M6 7h6M6 10h6M6 13h4"/></svg></div><h3>Safety</h3><p>Safe sites, trained crews and clear<br>checks at each stage of the build.</p></div>
  <div class="service" style="left:490px;top:187px"><div class="ico"><svg width="18" height="18" viewBox="0 0 18 18" fill="none" stroke="#fff" stroke-width="1.6"><rect x="3" y="8" width="12" height="8"/><path d="M6 8V5a3 3 0 0 1 6 0v3"/></svg></div><h3>Experience</h3><p>Years of brickwork on homes of every<br>size, from walls to whole builds.</p></div>
  <div class="service" style="left:727px;top:187px"><div class="ico"><svg width="18" height="18" viewBox="0 0 18 18" fill="none" stroke="#fff" stroke-width="1.6"><path d="M4 14l8-8m0 0 2-2 2 2-2 2m-2-2 2 2"/></svg></div><h3>Perfessional</h3><p>On time, on budget and in touch with<br>you through the whole project.</p></div>
  <div class="service" style="left:253px;top:359px"><div class="ico"><svg width="18" height="18" viewBox="0 0 18 18" fill="none" stroke="#fff" stroke-width="1.6"><rect x="3" y="4" width="12" height="11"/><path d="M3 8h12M6 2v4M12 2v4"/></svg></div><h3>Qualified Staff</h3><p>Licensed bricklayers and skilled<br>trades who know their craft well.</p></div>
  <div class="service" style="left:490px;top:359px"><div class="ico"><svg width="18" height="18" viewBox="0 0 18 18" fill="none" stroke="#fff" stroke-width="1.6"><circle cx="9" cy="9" r="6"/><path d="M6 9l2 2 4-4"/></svg></div><h3>Quality Work</h3><p>Straight lines, clean joints and a<br>finish that stands the test of time.</p></div>
  <div class="service" style="left:727px;top:359px"><div class="ico"><svg width="18" height="18" viewBox="0 0 18 18" fill="none" stroke="#fff" stroke-width="1.6"><path d="M4 14l8-8m-2-2 4 4"/></svg></div><h3>Delivery</h3><p>Materials on site when needed and<br>handover right when we promised.</p></div>
</section>

<h2 class="abs section-title portfolio-title">Portfolio</h2>
<div class="abs grid">
  <div role="img" aria-label="Modern angular building facade" style="background:linear-gradient(135deg,#6d5a40,#c9b48a)"></div>
  <div role="img" aria-label="Glass house with lawn and mountains" style="background:linear-gradient(180deg,#8fb0c8,#6f8f4a)"></div>
  <div role="img" aria-label="Lit modern villa at dusk" style="background:linear-gradient(160deg,#2d4a78,#c8904a)"></div>
  <div role="img" aria-label="Waterfront building at blue hour" style="background:linear-gradient(180deg,#2a5a9e,#0e2a5a)"></div>
  <div role="img" aria-label="Curved white architectural structure" style="background:linear-gradient(135deg,#dfe6ee,#7e95b5)"></div>
  <div role="img" aria-label="Timber house among trees" style="background:linear-gradient(160deg,#9bb0c0,#4a3a2a)"></div>
  <div role="img" aria-label="Stone house with pool and sea view" style="background:linear-gradient(180deg,#6fa6d6,#3a7ab8)"></div>
  <div role="img" aria-label="Bright open living room" style="background:linear-gradient(160deg,#e8e2d8,#b8a890)"></div>
</div>

<h2 class="abs section-title testi-title">Testimonials</h2>
<section class="abs testi">
  <q>Create with the heart; build with the mind.</q>
  <p>The crew turned up on time every day, kept the site tidy and built our extension exactly as planned. We would hire them again in a heartbeat.</p>
  <div class="dots"><span class="on"></span><span></span><span></span></div>
</section>

<section class="abs why">
  <div class="why-img" role="img" aria-label="Desk with plans, laptop, tape measure and folding ruler shaped as a house"></div>
  <div class="why-text">
    <h2>Why us?</h2>
    <h4>Because we are very flexible</h4>
    <p>We shape each job around you: your timeline, your budget and your home. Small repairs or full builds, we plan it with you first and keep you informed as the work moves ahead, with no surprises at the end.</p>
    <p>Our teams work across the region and can start soon. Ask us for a free quote or a friendly talk and we will visit, measure up and give you a clear price.</p>
  </div>
</section>

<h2 class="abs section-title news-title">Recent news</h2>
<div class="news" style="left:262px"><div class="ph" role="img" aria-label="Hands reviewing plans on a table"></div><h4>Prepare a room for painting</h4><p>Simple steps to clear, clean and patch walls before any new paint goes on.</p></div>
<div class="news" style="left:494px"><div class="ph" role="img" aria-label="Worker in hard hat on site" style="background:linear-gradient(135deg,#c8b070,#6a5a40)"></div><h4>Caring for construction</h4><p>How regular checks keep brick and mortar strong through every season.</p></div>
<div class="news" style="left:725px"><div class="ph" role="img" aria-label="Engineers working over drawings"></div><h4>Young engineers</h4><p>Meet the new team members bringing fresh skills to our growing crews.</p></div>

<section class="abs cta"><span>Pampered your brand with this beautiful theme just .</span><span class="btn">Read more</span></section>

<section class="abs contact">
  <h2 class="section-title">Contact us</h2>
  <div class="c-item" style="left:242px"><svg viewBox="0 0 28 28" fill="none" stroke="#0b4aa8" stroke-width="1.8"><path d="M14 25s8-8 8-14a8 8 0 0 0-16 0c0 6 8 14 8 14z"/><circle cx="14" cy="11" r="3"/></svg><h4>Visit our office</h4><p>48 Harrow Lane, 2nd Floor<br>Millbrook, MB 40213</p></div>
  <div class="c-item" style="left:427px"><svg viewBox="0 0 28 28" fill="none" stroke="#0b4aa8" stroke-width="1.8"><path d="M4 6h16v11H10l-6 5z"/><path d="M22 10h3v11l-3-2h-8"/></svg><h4>Let's talk</h4><p>Phone 1-555-014-2290<br>Fax 1-555-014-2291</p></div>
  <div class="c-item" style="left:614px"><svg viewBox="0 0 28 28" fill="none" stroke="#0b4aa8" stroke-width="1.8"><rect x="3" y="7" width="22" height="14"/><path d="M3 7l11 8 11-8"/></svg><h4>E-mail us</h4><p>hello@rtmarlow.example<br>jobs@rtmarlow.example</p></div>
  <div class="c-item" style="left:800px"><svg viewBox="0 0 28 28" fill="none" stroke="#0b4aa8" stroke-width="1.8"><path d="M5 13h4v11H5zM9 14l5-9c2 0 3 1 2 5h6c1 0 2 1 1 3l-2 8c0 1-1 2-2 2H9"/></svg><h4>Customer services</h4><p>Friendly help with quotes,<br>bookings and aftercare.</p></div>
</section>

<footer class="abs">
  <div class="social"><span></span><span></span><span></span><span></span></div>
  Copyrights R.T. Marlow © 2018
</footer>

</body>
</html>
```